Brambleton Business Card

I have a current card that I like it just needs a couple little changes to make it perfect. I would like the font size bigger so it could be easily read by older customers.

Business

```html
<!DOCTYPE html>
<html lang="en">
<head>
<meta charset="utf-8">
<title>Brambleton Motorsports and Marine – Business Card</title>
<link rel="stylesheet" href="https://fonts.googleapis.com/css2?family=Arimo:wght@400;700&family=Inter:wght@200;300&display=swap">
<style>
  :root {
    --card-black: #000000;
    --signal-yellow: #e6f51c;
    --paper-white: #f4f4f4;
    --mark-white: #ffffff;
  }
  html, body {
    margin: 0;
    padding: 0;
    width: 1200px;
    height: 700px;
    overflow: hidden;
    background: var(--card-black);
  }
  .business-card {
    position: relative;
    width: 1200px;
    height: 700px;
    background: var(--card-black);
    color: var(--paper-white);
    font-family: "Inter", Arial, sans-serif;
    font-weight: 300;
  }
  .business-card > * {
    position: absolute;
    margin: 0;
    white-space: nowrap;
    line-height: 1;
  }
  .company-name {
    left: 68px;
    top: 58px;
    font-family: "Arimo", Arial, sans-serif;
    font-weight: 700;
    font-size: 60px;
    color: var(--signal-yellow);
  }
  .website {
    left: 70px;
    top: 140px;
    font-size: 37px;
  }
  .phone-list {
    left: 720px;
    top: 140px;
    font-size: 37px;
    list-style: none;
    padding: 0;
  }
  .phone-list li { margin-bottom: 14px; }
  .phone-list .label { font-size: 28px; }
  .tagline {
    left: 528px;
    top: 300px;
    font-weight: 200;
    font-size: 48px;
    color: var(--signal-yellow);
  }
  .address {
    left: 720px;
    top: 408px;
    font-style: normal;
    font-size: 40px;
    line-height: 1.16;
  }
  .address sup { font-size: 19px; vertical-align: 18px; }
  .contact-name {
    left: 720px;
    top: 512px;
    font-family: "Arimo", Arial, sans-serif;
    font-weight: 700;
    font-size: 62px;
    color: var(--signal-yellow);
  }
  .email {
    left: 722px;
    top: 592px;
    font-size: 27px;
  }
  .brand-mark {
    left: 82px;
    top: 420px;
    display: flex;
    align-items: center;
    gap: 18px;
  }
  .brand-mark .dot {
    width: 46px;
    height: 46px;
    border-radius: 50%;
    background: var(--mark-white);
  }
  .brand-mark .wordmark {
    font-family: "Arimo", Arial, sans-serif;
    font-weight: 700;
    font-size: 52px;
    color: var(--mark-white);
  }
</style>
</head>
<body>
  <main class="business-card">
    <h1 class="company-name">Brambleton Motorsports and Marine</h1>
    <p class="website">www.brambletonmotorsports.com</p>
    <ul class="phone-list">
      <li>555-014-2207 <span class="label">phone</span></li>
      <li>555-014-1893 <span class="label">fax</span></li>
    </ul>
    <div class="brand-mark">
      <span class="dot"></span>
      <span class="wordmark">Brambleton</span>
    </div>
    <p class="tagline">FUN FOR ALL SEASONS</p>
    <address class="address">4821 118<sup>th</sup> Street West<br>Fairhaven, MN 55990</address>
    <p class="contact-name">Dale Harmon</p>
    <p class="email">dale@brambletonmotorsports.com</p>
  </main>
</body>
</html>
```